Varrow Business Card Design - Professional Flexible and forward thinking. Clean and Easy to follow

Management Consulting Company. I focus on business development and concept and operational review. I need a progressive, simple and professional layout design for the business cards, letterhead and envelops
Professional Flexible and forward thinking. Clean and Easy to follow
Mature Business persons and professionals and Corporations

Target Market(s)

Mature Business persons and professionals and Corporations - Government org.

Industry/Entity Type

Consulting

Contact Information for Business Card

Requirements
Must have
• Marcus Varrow
• President
• Phone - 347.682.1530
• email - Mvarrow@varrowpartners-example.com
• Skype - Marc.varrow
• 2187 Tollbrook Lane
• Suite A
• Cedarhaven, N.Y. 11492
• USA
Nice to have
• www.varrowpartners-example.com
Should not have
• N/A

```html
<!DOCTYPE html>
<html lang="en">
<head>
<meta charset="utf-8">
<title>Varrow Business Card Design</title>
<link rel="stylesheet" href="https://fonts.googleapis.com/css2?family=Arimo:wght@400;700&display=swap">
<style>
  :root {
    --yellow: #ffd400;
    --yellow-deep: #f6c000;
    --yellow-light: #fff6b8;
    --accent: #f5e600;
    --ink: #111111;
    --dark: #262626;
    --white: #ffffff;
    --rule: #8a8a8a;
    --band-start: #5a5548;
    --band-end: #b09a44;
  }
  * { margin: 0; padding: 0; box-sizing: border-box; }
  html, body { width: 1047px; height: 1200px; overflow: hidden; background: var(--white); }
  body { font-family: "Arimo", Arial, sans-serif; }
  .canvas { position: relative; width: 1047px; height: 1200px; overflow: hidden; }

  .card-front {
    position: absolute; left: 0; top: 0; width: 1047px; height: 599px;
    background: radial-gradient(ellipse 520px 300px at 50% 52%, var(--yellow-light) 0%, var(--yellow) 45%, var(--yellow-deep) 100%);
  }
  .brand { position: absolute; display: flex; align-items: center; font-weight: 700; white-space: nowrap; }
  .brand-square { border-radius: 8px; flex: none; }
  .brand-front { left: 178px; top: 255px; height: 87px; gap: 24px; color: var(--ink); font-size: 53px; letter-spacing: -0.3px; }
  .brand-front .brand-square { width: 86px; height: 87px; background: var(--ink); }

  .card-back {
    position: absolute; left: 0; top: 599px; width: 1047px; height: 601px;
    background: radial-gradient(ellipse 520px 360px at 50% 42%, #4c4c4c 0%, var(--dark) 80%);
  }
  .back-header {
    position: absolute; left: 0; top: 0; width: 100%; height: 135px;
    background: linear-gradient(#1f1f1f, #2a2a2a);
  }
  .header-sheen {
    position: absolute; left: 0; top: 135px; width: 100%; height: 36px;
    background: linear-gradient(#2c2c2c, #777 75%, #5a5a5a);
  }
  .brand-back { left: 122px; top: 23px; height: 101px; gap: 28px; color: var(--white); font-size: 61px; letter-spacing: -0.3px; }
  .brand-back .brand-square { width: 101px; height: 101px; background: linear-gradient(135deg, #fff45a, var(--accent)); }

  .person { position: absolute; left: 47px; top: 204px; width: 378px; }
  .person-name {
    color: var(--accent); font-weight: 700; font-size: 42px; line-height: 44px;
    padding-bottom: 4px; border-bottom: 1px solid var(--rule); white-space: nowrap;
  }
  .person-role { color: var(--white); font-size: 18px; margin-top: 8px; }

  .contacts { position: absolute; left: 48px; top: 350px; list-style: none; }
  .contacts li { display: flex; align-items: center; height: 52px; color: var(--white); font-size: 29px; white-space: nowrap; }
  .contacts svg { width: 33px; height: 33px; margin-right: 16px; flex: none; }

  .address { position: absolute; left: 640px; top: 253px; color: var(--white); font-size: 30px; line-height: 36.5px; font-style: normal; }

  .footer-band {
    position: absolute; left: 0; top: 540px; width: 517px; height: 36px;
    background: linear-gradient(90deg, var(--band-start), var(--band-end));
  }
  .footer-url {
    position: absolute; left: 517px; top: 540px; width: 530px; height: 36px;
    background: linear-gradient(90deg, #d8c22e, var(--yellow) 60%, #fff200);
    color: var(--ink); font-size: 28px; line-height: 36px; text-align: right; padding-right: 55px;
  }
</style>
</head>
<body>
<div class="canvas">
  <section class="card-front">
    <div class="brand brand-front"><span class="brand-square"></span><span>VARROW ASSOCIATES</span></div>
  </section>

  <section class="card-back">
    <div class="back-header"></div>
    <div class="header-sheen"></div>
    <div class="brand brand-back"><span class="brand-square"></span><span>VARROW ASSOCIATES</span></div>

    <div class="person">
      <div class="person-name">MARCUS VARROW</div>
      <div class="person-role">President</div>
    </div>

    <ul class="contacts">
      <li>
        <svg viewBox="0 0 32 32" aria-hidden="true"><circle cx="16" cy="16" r="14" fill="none" stroke="#fff" stroke-width="2.2"/><path d="M11 8.5c1 0 1.5.3 2 1.5l1 2.5c.3.8 0 1.4-.6 1.9l-1 .8c.8 1.8 2.2 3.3 3.9 4.2l.9-1c.5-.6 1.1-.8 1.9-.5l2.4 1c1.1.5 1.4 1 1.4 2 0 1.8-1.8 3-3.6 2.7C14 22.6 9.5 18 8.8 12.2 8.5 10.3 9.4 8.5 11 8.5z" fill="#fff"/></svg>
        347.682.1530
      </li>
      <li>
        <svg viewBox="0 0 32 32" aria-hidden="true"><rect x="2" y="7" width="28" height="19" fill="none" stroke="#fff" stroke-width="2.2"/><path d="M2 7l14 11 14-11M2 26l10-9M30 26l-10-9" fill="none" stroke="#fff" stroke-width="2"/></svg>
        Mvarrow@varrowpartners-example.com
      </li>
      <li>
        <svg viewBox="0 0 32 32" aria-hidden="true"><circle cx="16" cy="16" r="14" fill="#fff"/></svg>
        Marc.varrow
      </li>
    </ul>

    <address class="address">
      2187 Tollbrook Lane<br>
      Suite A<br>
      Cedarhaven, N.Y. 11492<br>
      USA
    </address>

    <div class="footer-band" role="img" aria-label="Decorative footer band in grey-gold tones"></div>
    <div class="footer-url">www.varrowpartners-example.com</div>
  </section>
</div>
</body>
</html>
```